" Um **Cartório de Registro Civil** e **Tabelionato de Notas** são serviços essenciais no Brasil, responsáveis por formalizar e garantir a autenticidade de diversos atos e documentos jurídicos. Esses serviços possuem funções distintas, mas ambos têm um papel crucial na organização e segurança dos registros públicos. ### Cartório de Registro Civil: Este cartório é responsável pelo registro de fatos da vida civil das pessoas. Suas principais atividades incluem: 1. **Registro de Nascimento**: Formaliza o nascimento de uma pessoa, atribuindo-lhe um nome e identidade legal. 2. **Registro de Casamento**: Oficializa a união entre duas pessoas, criando um vínculo jurídico entre elas. 3. **Registro de Óbito**: Documenta a morte de uma pessoa, permitindo a regularização de heranças e outros direitos relacionados. 4. **Emissão de Certidões**: As certidões de nascimento, casamento e óbito são documentos solicitados frequentemente para diversos fins, como processos judiciais, registros administrativos, e outros. Além disso, o Registro Civil também pode realizar registros de emancipação, interdições e retificações de registro, como, por exemplo, corrigir erros materiais nos registros. ### Tabelionato de Notas: O Tabelionato de Notas é um serviço onde são lavradas e autenticadas diversas escrituras e documentos, conferindo-lhes a segurança jurídica necessária para garantir a veracidade e legalidade. Entre as funções mais comuns, destacam-se: 1. **Reconhecimento de Firmas**: Serve para autenticar a assinatura de uma pessoa em documentos, confirmando que a assinatura foi feita de próprio punho. 2. **Lavratura de Escrituras**: Inclui escrituras de compra e venda de imóveis, de doação, de constituição de empresa, entre outras. Essas escrituras formalizam acordos entre partes, tornando-os válidos juridicamente. 3. **Procurações**: Documento que confere poderes a uma pessoa para agir em nome de outra, seja para fins administrativos ou legais. 4. **Autenticação de Documentos**: Confirma que uma cópia de um documento é fiel ao original. 5. **Testamentos**: O Tabelião também pode lavrar testamentos, que são declarações de vontade de uma pessoa sobre a disposição de seus bens após a morte. Ambos os cartórios devem seguir normas e procedimentos rigorosos para garantir a validade dos atos que realizam. São estabelecimentos públicos, mas prestam serviços pagos, sendo supervisionados pelo poder judiciário e pelas corregedorias estaduais para garantir que a legislação seja cumprida corretamente. O trabalho desses cartórios é essencial para assegurar os direitos e deveres dos cidadãos e a segurança jurídica dos atos que realizam, sendo fundamentais para a organização da vida civil no Brasil. "

```html
<!DOCTYPE html>
<html lang="pt-BR">
<head>
<meta charset="utf-8">
<title>Papel timbrado – Cartório Helena Prado</title>
<link rel="stylesheet" href="https://fonts.googleapis.com/css2?family=Cinzel:wght@600&family=Montserrat:wght@400;600;700&family=Mrs+Saint+Delafield&display=swap">
<style>
  :root {
    --backdrop: #e9e6e1;
    --paper: #ffffff;
    --ink: #1f1f1f;
    --ink-soft: #444444;
    --gold: #b58a45;
    --gold-light: #d6b27a;
    --gold-dark: #8c6630;
  }
  * { margin: 0; padding: 0; box-sizing: border-box; }
  html, body {
    width: 1200px; height: 1200px; overflow: hidden;
    background: var(--backdrop);
  }
  .canvas {
    width: 1200px; height: 1200px;
    display: flex; align-items: center; justify-content: center;
  }
  .letterhead {
    position: relative;
    width: 806px; height: 1140px;
    background: var(--paper);
    box-shadow: 0 6px 24px rgba(0,0,0,.12);
    font-family: "Montserrat", sans-serif;
    color: var(--ink);
    overflow: hidden;
  }
  .brand {
    position: absolute; top: 118px; left: 0; right: 0;
    text-align: center;
  }
  .brand-mark {
    display: block; width: 34px; height: 34px; margin: 0 auto 12px;
    border-radius: 50%; background: var(--gold);
  }
  .brand-name {
    font-family: "Cinzel", serif; font-weight: 600;
    color: var(--ink); line-height: 1;
  }
  .brand-name .brand-kind { display: block; font-size: 15px; letter-spacing: 4px; margin-bottom: 6px; }
  .brand-name .brand-title { display: block; font-size: 40px; letter-spacing: 1px; }
  .brand-tagline {
    margin-top: 8px; font-size: 7.5px; font-weight: 600;
    letter-spacing: 1.4px; text-transform: uppercase; color: var(--ink-soft);
  }
  .recipient {
    position: absolute; top: 330px; left: 78px;
    font-size: 10px; line-height: 15px;
  }
  .recipient .to-label { font-weight: 700; font-size: 11.5px; }
  .recipient .recipient-name { font-weight: 700; }
  .letter-body {
    position: absolute; top: 448px; left: 78px; width: 650px;
    font-size: 10px; line-height: 15px; color: var(--ink-soft);
  }
  .letter-body p { margin-bottom: 12px; }
  .sign-off {
    position: absolute; top: 868px; left: 78px;
  }
  .signature {
    font-family: "Mrs Saint Delafield", cursive;
    font-size: 44px; color: var(--ink); line-height: 1;
  }
  .signer { margin-top: 10px; font-size: 10px; line-height: 14px; }
  .signer-name { font-weight: 700; }
  .contact-bar {
    position: absolute; top: 992px; left: 160px; right: 60px;
    display: flex; gap: 38px; font-size: 9px; line-height: 13px;
    color: var(--ink-soft);
  }
  .contact-item { display: flex; align-items: flex-start; gap: 8px; }
  .contact-item svg { width: 15px; height: 15px; flex: none; margin-top: 3px; fill: var(--ink); }
  .footer-band {
    position: absolute; left: 0; right: 0; bottom: 0; height: 32px;
    background: linear-gradient(90deg, var(--gold-dark), var(--gold-light) 50%, var(--gold-dark));
  }
</style>
</head>
<body>
<main class="canvas">
  <article class="letterhead">
    <header class="brand">
      <span class="brand-mark"></span>
      <h1 class="brand-name">
        <span class="brand-kind">CARTÓRIO</span>
        <span class="brand-title">HELENA PRADO</span>
      </h1>
      <p class="brand-tagline">Cartório de Registro Civil e Tabelionato de Notas</p>
    </header>

    <address class="recipient" style="font-style:normal">
      <div class="to-label">TO</div>
      <div class="recipient-name">Paulo Andrade Reis</div>
      <div>Recursos Humanos</div>
      <div>Norte Vale Ltda</div>
      <div>Rua das Acácias, 245</div>
      <div>Curitiba, PR</div>
    </address>

    <section class="letter-body">
      <p>Prezado senhor, agradecemos o contato e a confiança depositada em nossa equipe. Conforme solicitado, encaminhamos as informações sobre os serviços de registro civil e de notas prestados por este cartório, que incluem registros de nascimento, casamento e óbito, emissão de certidões, reconhecimento de firmas, lavratura de escrituras, procurações, autenticação de documentos e testamentos. Todos os atos seguem normas rigorosas e são supervisionados pela corregedoria estadual, garantindo validade e segurança jurídica a cada documento emitido.</p>
      <p>Nosso atendimento funciona de segunda a sexta-feira, das nove às dezessete horas, com agendamento prévio disponível pelo telefone ou pelo endereço eletrônico indicados abaixo.</p>
      <p>Estamos à disposição para esclarecer qualquer dúvida.</p>
      <p>Para a lavratura de escrituras de compra e venda, doação ou constituição de empresa, solicitamos a apresentação dos documentos pessoais das partes, certidões atualizadas do imóvel e comprovantes de quitação de tributos. Nos casos de procuração, é necessária a presença do outorgante, que deverá portar documento oficial com foto. Os reconhecimentos de firma podem ser realizados por semelhança ou por autenticidade, conforme a exigência do órgão de destino.</p>
      <p>As certidões de nascimento, casamento e óbito podem ser solicitadas presencialmente ou de forma eletrônica, com prazo médio de entrega de três dias úteis. Retificações, registros de emancipação e averbações de divórcio também são atendidos por nossa equipe, que acompanha cada etapa do processo até a entrega final do documento ao interessado.</p>
      <p>Atenciosamente, aguardamos seu retorno para dar andamento à solicitação.</p>
    </section>

    <div class="sign-off">
      <div class="signature">Rafael Moura</div>
      <div class="signer">
        <div class="signer-name">Rafael Moura</div>
        <div>Managing Director</div>
      </div>
    </div>

    <footer class="contact-bar">
      <div class="contact-item">
        <svg viewBox="0 0 24 24" aria-hidden="true"><path d="M6.6 10.8a15.2 15.2 0 0 0 6.6 6.6l2.2-2.2c.3-.3.7-.4 1-.2 1.1.4 2.3.6 3.6.6.6 0 1 .4 1 1V20c0 .6-.4 1-1 1A17 17 0 0 1 3 4c0-.6.4-1 1-1h3.5c.6 0 1 .4 1 1 0 1.3.2 2.5.6 3.6.1.3 0 .7-.2 1z"/></svg>
        <div>+55 (41) 3322-4810<br>+55 (41) 98844-2107</div>
      </div>
      <div class="contact-item">
        <svg viewBox="0 0 24 24" aria-hidden="true"><path d="M12 2a10 10 0 1 0 0 20 10 10 0 0 0 0-20zm6.9 6h-2.9a15.6 15.6 0 0 0-1.4-3.6A8 8 0 0 1 18.9 8zM12 4c.8 1.2 1.5 2.5 1.9 4h-3.8c.4-1.5 1.1-2.8 1.9-4zM4.3 14a8.2 8.2 0 0 1 0-4h3.4a16.5 16.5 0 0 0 0 4zm.8 2h2.9c.3 1.3.8 2.5 1.4 3.6A8 8 0 0 1 5.1 16zM8 8H5.1a8 8 0 0 1 4.3-3.6C8.8 5.5 8.3 6.7 8 8zm4 12c-.8-1.2-1.5-2.5-1.9-4h3.8c-.4 1.5-1.1 2.8-1.9 4zm2.3-6H9.7a14.7 14.7 0 0 1 0-4h4.6a14.7 14.7 0 0 1 0 4zm.3 5.6c.6-1.1 1.1-2.3 1.4-3.6h2.9a8 8 0 0 1-4.3 3.6zm1.7-5.6a16.5 16.5 0 0 0 0-4h3.4a8.2 8.2 0 0 1 0 4z"/></svg>
        <div>contato@helenaprado.com.br<br>www.helenaprado.com.br</div>
      </div>
      <div class="contact-item">
        <svg viewBox="0 0 24 24" aria-hidden="true"><path d="M12 2a7 7 0 0 0-7 7c0 5.2 7 13 7 13s7-7.8 7-13a7 7 0 0 0-7-7zm0 9.5a2.5 2.5 0 1 1 0-5 2.5 2.5 0 0 1 0 5z"/></svg>
        <div>Av. das Palmeiras, 480<br>Centro<br>80020-310 - Curitiba / PR</div>
      </div>
    </footer>

    <div class="footer-band"></div>
  </article>
</main>
</body>
</html>
```